New nutrition counseling business needs a flyer and logo design for marketing purposes

Need a new flyer for distribution to advertise and inform the public about new Dietetic Counseling service. The new business name is Harbor of Vigor with “Harbor” being the main name. It will provide nutrition consultation services to individuals who seek to change their dietary habits to achieve a variety of different health objectives. These objectives can include, but are not limited to weight management, enhanced athletic performance, improved health biomarkers, and reducing the risks or symptoms of chronic nutrition related diseases. The services provided include direct one on one counseling that entails health and nutrition assessments, evaluation of goals, and the determination of strategies to meet these goals. We would like to see designs that use an ocean color scheme with purple aspects as well. Color and logo ideas attached in uploads. Please include logo on the flyer as well.

Target Market(s)

General Population

Colors
0094D4
00A9DD
6FCCEA
C7EBF8
E9F6FB
00AB8E
00BBA5
67D7C9
C6EFE9
E9F9F6
6B429C
8869AF
B7A5CE
E3DAEB
F3F0F8

Requirements
Nice to have
• Pictures of nourishing foods, fruits, vegetables etc.
Should not have
• Do not include people in flyer or logo design

```html
<!DOCTYPE html>
<html lang="en">
<head>
<meta charset="utf-8">
<title>Harbor of Vigor – Nutrition Counseling Flyer</title>
<link rel="stylesheet" href="https://fonts.googleapis.com/css2?family=Poppins:wght@400;500;600;700;800&display=swap">
<style>
  :root {
    --backdrop: #d2d2d2;
    --paper: #ffffff;
    --ocean-blue: #0094d4;
    --sky-blue: #00a9dd;
    --light-blue: #6fccea;
    --teal: #00ab8e;
    --sea-green: #00bba5;
    --mint: #67d7c9;
    --purple: #6b429c;
    --lavender: #8869af;
    --lilac: #b7a5ce;
    --ink: #2e2e2e;
    --font: "Poppins", sans-serif;
  }
  * { box-sizing: border-box; margin: 0; padding: 0; }
  html, body { width: 685px; height: 1200px; overflow: hidden; }
  body { background: var(--backdrop); font-family: var(--font); position: relative; }

  .flyer {
    position: absolute; left: 12px; top: 134px;
    width: 660px; height: 932px;
    background: var(--paper); overflow: hidden;
    box-shadow: 0 6px 18px rgba(0,0,0,.25);
  }
  .abs { position: absolute; }

  .hero-art { position: absolute; left: 0; top: 0; width: 660px; height: 420px; }

  .brand { left: 40px; top: 66px; display: flex; align-items: center; gap: 9px; }
  .brand-dot { width: 26px; height: 26px; border-radius: 50%; border: 3px solid var(--sea-green); }
  .brand-name { font-size: 21px; font-weight: 700; color: var(--ocean-blue); line-height: 1.1; }

  .kicker { left: 40px; top: 172px; font-size: 25px; font-weight: 700; color: var(--teal); line-height: 1.2; }
  .headline { left: 37px; top: 203px; font-size: 72px; font-weight: 800; color: var(--sky-blue); letter-spacing: 1px; line-height: 1; }
  .tag-band {
    left: 40px; top: 269px; width: 264px; height: 27px; background: var(--purple);
    color: #fff; font-size: 13px; font-weight: 500; letter-spacing: 5.2px;
    display: flex; align-items: center; justify-content: center;
  }
  .subline { left: 40px; top: 305px; font-size: 17px; color: var(--ink); }

  .counselor { left: 41px; top: 350px; }
  .counselor-first { font-size: 20px; font-weight: 700; color: var(--sky-blue); line-height: 1.05; }
  .counselor-last { font-size: 20px; font-weight: 700; color: var(--teal); line-height: 1.05; }
  .credentials { font-size: 8px; font-weight: 600; color: var(--ink); margin-top: 1px; }
  .license { display: flex; margin-top: 2px; height: 12px; border-radius: 6px; overflow: hidden; font-size: 7px; color: #fff; font-weight: 500; width: max-content; }
  .license span { display: flex; align-items: center; padding: 0 9px; }
  .license .label { background: var(--ocean-blue); }
  .license .number { background: var(--sea-green); }

  .divider-v { width: 1.5px; background: var(--ocean-blue); }
  .degree { left: 290px; top: 383px; font-size: 15px; font-weight: 500; color: var(--ink); display: flex; align-items: center; }
  .degree::before { content: ""; position: absolute; left: -18px; border-left: 6px solid var(--ocean-blue); border-top: 5px solid transparent; border-bottom: 5px solid transparent; }

  .photo { border-radius: 50%; }
  .almonds { left: -31px; top: 430px; width: 80px; height: 80px; background: radial-gradient(circle, #9a5c3a, #6e3a22); }
  .services-band {
    left: 45px; top: 455px; width: 236px; height: 38px; background: var(--purple);
    color: #fff; font-size: 21px; font-weight: 700; display: flex; align-items: center; justify-content: center;
  }
  .herb { left: 300px; top: 448px; width: 118px; height: 50px; border-radius: 50% 50% 50% 50% / 60% 60% 40% 40%;
    background: linear-gradient(120deg, #4f7d2f, #8bb35a); transform: rotate(-8deg); }

  .service-list { left: 44px; top: 518px; width: 340px; list-style: none; }
  .service-list li { display: flex; gap: 6px; font-size: 12px; line-height: 14px; color: var(--ink); margin-bottom: 6.5px; }
  .service-list svg { flex: 0 0 11px; margin-top: 1px; }
  .service-list .narrow { width: 218px; }

  .hummus { left: 273px; top: 573px; width: 144px; height: 144px; border: 4px solid #6f8a86;
    background: radial-gradient(circle at 50% 45%, #f3d37c, #e8b955 60%, #c9a46b); }

  .modes { left: 450px; top: 455px; }
  .modes .line1 { font-size: 17px; color: var(--purple); line-height: 1.1; }
  .modes .line2 { font-size: 17px; font-weight: 600; color: var(--sea-green); line-height: 1.1; }
  .modes .line2 .amp { color: var(--lavender); font-weight: 400; }
  .modes .line3 { font-size: 13.5px; color: var(--purple); line-height: 1.1; }
  .modes .line4 { font-size: 32px; font-weight: 800; color: var(--sky-blue); line-height: 1.05; }

  .chat-card { left: 436px; top: 578px; width: 182px; height: 136px; border: 1.5px solid var(--light-blue); border-radius: 12px; border-top-left-radius: 0; border-left: none; }
  .chat-title { left: 486px; top: 588px; font-size: 19px; font-weight: 700; color: var(--sea-green); }
  .chat-icon { left: 437px; top: 584px; }
  .offer-free { left: 436px; top: 622px; font-size: 21px; font-weight: 700; color: var(--lavender); }
  .offer-num { left: 434px; top: 645px; font-size: 46px; font-weight: 800; color: var(--sea-green); line-height: 1; letter-spacing: -1px; }
  .offer-unit { left: 437px; top: 692px; font-size: 10px; font-weight: 600; color: var(--sea-green); }
  .offer-text { left: 502px; top: 628px; font-size: 13.5px; font-weight: 500; color: var(--purple); line-height: 15.8px; }

  .contact-label { left: 286px; top: 748px; font-size: 23px; color: var(--ink); display: flex; align-items: center; gap: 6px; }
  .contact-label::after { content: ""; border-left: 6px solid var(--ocean-blue); border-top: 6px solid transparent; border-bottom: 6px solid transparent; }
  .phone { left: 419px; top: 743px; font-size: 27px; font-weight: 700; color: var(--ink); letter-spacing: .5px; }
  .email { left: 419px; top: 778px; font-size: 16.5px; font-weight: 500; color: var(--ink); }

  .bowl-grains { left: -9px; top: 721px; width: 270px; height: 270px; background: conic-gradient(#a7d06b, #e9c46a, #6b2a2f, #7a4a8c, #b9cf75, #a7d06b); }
  .bowl-veg { left: 248px; top: 802px; width: 162px; height: 162px; background: conic-gradient(#d9453b, #f1d36d, #9bbf5a, #eadbb6, #d9453b); }
  .veg-scatter { left: 400px; top: 800px; width: 300px; height: 150px; border-radius: 60% 0 0 0;
    background: linear-gradient(160deg, rgba(255,255,255,0) 10%, #f2a33a 45%, #6a9c3d 70%, #e8e4dc); }
  .edge-veg { left: 630px; top: 700px; width: 55px; height: 100px; border-radius: 30px 0 0 30px;
    background: linear-gradient(180deg, #d83a35, #e8892f, #7a7a7a); }
</style>
</head>
<body>
<main class="flyer">
  <svg class="hero-art" viewBox="0 0 660 420">
    <defs>
      <radialGradient id="vegGlow" cx="50%" cy="55%" r="60%">
        <stop offset="0%" stop-color="#7fb443"/>
        <stop offset="55%" stop-color="#4f8f2e"/>
        <stop offset="80%" stop-color="#d8453a"/>
        <stop offset="100%" stop-color="#f3c530"/>
      </radialGradient>
    </defs>
    <circle cx="492" cy="198" r="187" fill="var(--mint)"/>
    <circle cx="506" cy="180" r="172" fill="#ffffff"/>
    <circle cx="506" cy="180" r="160" fill="url(#vegGlow)" role="img" aria-label="Basket of fresh vegetables and fruit: peppers, greens, cauliflower, apples"/>
    <ellipse cx="330" cy="48" rx="24" ry="52" transform="rotate(40 330 48)" fill="var(--lilac)" role="img" aria-label="Large leaf shape"/>
    <ellipse cx="350" cy="110" rx="18" ry="50" transform="rotate(20 350 110)" fill="var(--lavender)" role="img" aria-label="Leaf shape"/>
    <ellipse cx="642" cy="340" rx="20" ry="32" transform="rotate(25 642 340)" fill="var(--sea-green)" role="img" aria-label="Leaf shape"/>
  </svg>

  <div class="abs brand">
    <span class="brand-dot"></span>
    <span class="brand-name">Harbor of Vigor</span>
  </div>

  <p class="abs kicker">Helping clients</p>
  <h1 class="abs headline">FOSTER</h1>
  <div class="abs tag-band">POSITIVE NUTRITION</div>
  <p class="abs subline">Practices for a healthier lifestyle</p>

  <div class="abs counselor">
    <div class="counselor-first">Marisol</div>
    <div class="counselor-last">Delgado</div>
    <div class="credentials">MS, RD, LD/N</div>
    <div class="license"><span class="label">License Number</span><span class="number">ND 20417</span></div>
  </div>
  <div class="abs divider-v" style="left:272px;top:362px;height:63px;"></div>
  <p class="abs degree">Master of Science in Dietetics and Nutrition</p>

  <div class="abs photo almonds" role="img" aria-label="Bowl of almonds"></div>
  <h2 class="abs services-band">SERVICES OFFERED</h2>
  <div class="abs herb" role="img" aria-label="Fresh basil sprig"></div>

  <ul class="abs service-list">
    <li><svg width="11" height="11" viewBox="0 0 11 11"><rect x=".6" y=".6" width="9.8" height="9.8" rx="1.5" fill="none" stroke="#0094d4" stroke-width="1.2"/><path d="M2.5 5.6l2 2 4-4.5" fill="none" stroke="#0094d4" stroke-width="1.5"/></svg><span>Medical Nutrition Therapy for chronic conditions such as diabetes, hypertension, high cholesterol, and more</span></li>
    <li><svg width="11" height="11" viewBox="0 0 11 11"><rect x=".6" y=".6" width="9.8" height="9.8" rx="1.5" fill="none" stroke="#0094d4" stroke-width="1.2"/><path d="M2.5 5.6l2 2 4-4.5" fill="none" stroke="#0094d4" stroke-width="1.5"/></svg><span>Weight Management</span></li>
    <li><svg width="11" height="11" viewBox="0 0 11 11"><rect x=".6" y=".6" width="9.8" height="9.8" rx="1.5" fill="none" stroke="#0094d4" stroke-width="1.2"/><path d="M2.5 5.6l2 2 4-4.5" fill="none" stroke="#0094d4" stroke-width="1.5"/></svg><span>Healthy Eating and Meal Planning</span></li>
    <li><svg width="11" height="11" viewBox="0 0 11 11"><rect x=".6" y=".6" width="9.8" height="9.8" rx="1.5" fill="none" stroke="#0094d4" stroke-width="1.2"/><path d="M2.5 5.6l2 2 4-4.5" fill="none" stroke="#0094d4" stroke-width="1.5"/></svg><span>Nutrition for Athletic Performance</span></li>
    <li><svg width="11" height="11" viewBox="0 0 11 11"><rect x=".6" y=".6" width="9.8" height="9.8" rx="1.5" fill="none" stroke="#0094d4" stroke-width="1.2"/><path d="M2.5 5.6l2 2 4-4.5" fill="none" stroke="#0094d4" stroke-width="1.5"/></svg><span>Pre and Post Natal Nutrition</span></li>
    <li class="narrow"><svg width="11" height="11" viewBox="0 0 11 11"><rect x=".6" y=".6" width="9.8" height="9.8" rx="1.5" fill="none" stroke="#0094d4" stroke-width="1.2"/><path d="M2.5 5.6l2 2 4-4.5" fill="none" stroke="#0094d4" stroke-width="1.5"/></svg><span>Personalized meal plans uniquely catered to each individual</span></li>
    <li class="narrow"><svg width="11" height="11" viewBox="0 0 11 11"><rect x=".6" y=".6" width="9.8" height="9.8" rx="1.5" fill="none" stroke="#0094d4" stroke-width="1.2"/><path d="M2.5 5.6l2 2 4-4.5" fill="none" stroke="#0094d4" stroke-width="1.5"/></svg><span>Highly collaborative approach to help you meet your goals</span></li>
  </ul>

  <div class="abs photo hummus" role="img" aria-label="Bowl of hummus topped with chickpeas"></div>

  <div class="abs divider-v" style="left:438px;top:461px;height:76px;"></div>
  <div class="abs modes">
    <div class="line1">Both in</div>
    <div class="line2">PERSON <span class="amp">&amp;</span> VIRTUAL</div>
    <div class="line3">consultations are</div>
    <div class="line4">OFFERED</div>
  </div>

  <div class="abs chat-card"></div>
  <svg class="abs chat-icon" width="44" height="32" viewBox="0 0 44 32">
    <ellipse cx="26" cy="12" rx="14" ry="10" fill="var(--sky-blue)"/>
    <ellipse cx="16" cy="17" rx="14" ry="11" fill="var(--sea-green)" stroke="#fff" stroke-width="2"/>
    <path d="M8 25l-3 6 8-4z" fill="var(--sea-green)"/>
    <circle cx="10" cy="17" r="1.8" fill="#fff"/><circle cx="16" cy="17" r="1.8" fill="#fff"/><circle cx="22" cy="17" r="1.8" fill="#fff"/>
  </svg>
  <p class="abs chat-title">Let’s Chat!</p>
  <p class="abs offer-free">FREE</p>
  <p class="abs offer-num">15</p>
  <p class="abs offer-unit">MINUTES</p>
  <p class="abs offer-text">introductory<br>consultation<br>to discuss<br>program details<br>and rates</p>

  <div class="abs edge-veg" role="img" aria-label="Fresh tomatoes and vegetables at the page edge"></div>
  <div class="abs veg-scatter" role="img" aria-label="Scattered vegetables: carrots, eggplant, beans, leaves"></div>
  <div class="abs photo bowl-grains" role="img" aria-label="Grain bowl with avocado, chickpeas, beans, cabbage and sprouts"></div>
  <div class="abs photo bowl-veg" role="img" aria-label="Bowl of tomatoes, lemon and cauliflower"></div>

  <p class="abs contact-label">Contact</p>
  <p class="abs phone">555-014-2287</p>
  <p class="abs email">marisol@delgadord.net</p>
</main>
</body>
</html>
```